Business Cards

The name of our firm is "Tallpine Insurance adjusters"
We separate ourselves from all other public adjusters because most of us worked for the insurance companies so we understand their games.
As Insurance adjusters we represent the Insured, not the insurance companies. Our # 1 priority is to handle the entire claim process as seamless as possible on behalf of the homeowner/business owner so they don't have to deal with the hassles and headaches. Just as the logo your team designed, I want the cards to stand out from everyone elses. I also want the cards to help better understand our services and Value on hiring us and value that we can offer.
I uploaded the logo whenever I created the project. I don't see an option on re uploading the logo anywhere. Any advise??

```html
<!DOCTYPE html>
<html lang="en">
<head>
<meta charset="utf-8">
<title>Tallpine Insurance Adjusters – Business Cards</title>
<link rel="stylesheet" href="https://fonts.googleapis.com/css2?family=Montserrat:wght@400;500;700;800&display=swap">
<style>
  :root {
    --page-bg: #d4d4d4;
    --card-bg: #111112;
    --brand-blue: #0a72b3;
    --text-light: #ececec;
    --rule-blue: #0b5f93;
  }
  * { box-sizing: border-box; margin: 0; padding: 0; }
  html, body {
    width: 1200px; height: 800px; overflow: hidden;
    background: var(--page-bg);
    font-family: "Montserrat", Arial, sans-serif;
  }
  .canvas {
    width: 1200px; height: 800px;
    display: flex; flex-direction: column;
    align-items: center; justify-content: center; gap: 34px;
  }
  .card {
    position: relative;
    width: 600px; height: 343px;
    background: var(--card-bg);
    border-bottom: 11px solid var(--brand-blue);
    box-shadow: 0 8px 24px rgba(0,0,0,.25);
    overflow: hidden;
  }
  /* Brand name set as plain text */
  .brand-name {
    color: var(--brand-blue);
    font-weight: 800;
    text-transform: uppercase;
    text-align: center;
    line-height: 1.1;
  }
  .card-front { display: flex; align-items: center; justify-content: center; }
  .card-front .brand-name { font-size: 40px; letter-spacing: 1px; }
  .card-front .brand-name small { display: block; font-size: 15px; letter-spacing: 3px; margin-top: 6px; }

  .card-contact .brand-name {
    position: absolute; top: 40px; right: 42px;
    font-size: 24px; text-align: right;
  }
  .card-contact .brand-name small { display: block; font-size: 9px; letter-spacing: 2px; margin-top: 4px; }

  .divider {
    position: absolute; left: 36px; right: 36px; top: 178px;
    height: 1px; background: var(--rule-blue);
  }
  .person { position: absolute; left: 36px; top: 118px; }
  .person-name {
    color: var(--brand-blue); font-weight: 700; font-size: 24px;
    text-transform: uppercase; letter-spacing: .5px;
  }
  .person-title { color: var(--text-light); font-size: 15px; font-weight: 500; margin-top: 2px; }

  .contact-list {
    position: absolute; left: 36px; top: 196px;
    list-style: none; display: flex; flex-direction: column; gap: 7px;
  }
  .contact-list li {
    display: flex; align-items: center; gap: 10px;
    color: var(--text-light); font-size: 15px; font-weight: 500;
  }
  .contact-list svg { width: 15px; height: 15px; flex: none; }

  .address {
    position: absolute; right: 36px; top: 200px;
    color: var(--text-light); font-size: 14px; font-weight: 500;
    line-height: 1.5; text-align: right;
  }
</style>
</head>
<body>
<main class="canvas">

  <section class="card card-contact" aria-label="Business card, contact side">
    <p class="brand-name">Tallpine<small>Insurance Adjusters</small></p>

    <div class="person">
      <p class="person-name">Daniel Harper</p>
      <p class="person-title">Managing Director</p>
    </div>

    <div class="divider"></div>

    <ul class="contact-list">
      <li>
        <svg viewBox="0 0 24 24" aria-hidden="true"><path fill="var(--brand-blue)" d="M6.6 10.8a15.1 15.1 0 0 0 6.6 6.6l2.2-2.2a1 1 0 0 1 1-.25 11.4 11.4 0 0 0 3.6.57 1 1 0 0 1 1 1V20a1 1 0 0 1-1 1A17 17 0 0 1 3 4a1 1 0 0 1 1-1h3.5a1 1 0 0 1 1 1c0 1.25.2 2.45.57 3.57a1 1 0 0 1-.25 1z"/></svg>
        000 XXX 0000
      </li>
      <li>
        <svg viewBox="0 0 24 24" aria-hidden="true"><rect x="2" y="5" width="20" height="14" fill="var(--brand-blue)"/><path d="M2 5l10 8 10-8" fill="none" stroke="var(--card-bg)" stroke-width="1.8"/></svg>
        email@websitename.com
      </li>
      <li>
        <svg viewBox="0 0 24 24" aria-hidden="true"><circle cx="12" cy="12" r="10" fill="var(--brand-blue)"/><g fill="none" stroke="var(--card-bg)" stroke-width="1.4"><ellipse cx="12" cy="12" rx="4" ry="10"/><path d="M2 12h20M4 7h16M4 17h16"/></g></svg>
        www.websitename.com
      </li>
    </ul>

    <p class="address">Adress line here with<br>country pincode 000021</p>
  </section>

  <section class="card card-front" aria-label="Business card, brand side">
    <p class="brand-name">Tallpine<small>Insurance Adjusters</small></p>
  </section>

</main>
</body>
</html>
```